Unique & Creative Business Card for Lumivaleta

Would you please create a unique design that is soft and appealing to people who seek to raise vibrational energy for themselves, for animals (domestic or wild), or for the environment.

Optional: Elements could include, landscapes, wild animals, feathers, vibrational patterns, the elements (Earth, water, fire, air and space). Images that are calming.

With Thanks!

Target Market(s)

People and businesses who are into the environment, animal welfare, alternative health.

Contact Information for Business Card

Moira Tess
Energist
mt@lumivaleta.example
lumivaleta.example

Requirements
Must have
• Lumivaleta logo (attached)
Symbols that represent our main services: Natural environment, animal, human and energy.
Our strapline ‘Achieving Vibrational Equilibrium’
Nice to have
• Clear and easy to read
Colours based on nature/soft colours

```html
<!DOCTYPE html>
<html lang="en">
<head>
<meta charset="utf-8">
<title>Lumivaleta – Business Card</title>
<link rel="stylesheet" href="https://fonts.googleapis.com/css2?family=Roboto:wght@500&family=Roboto+Condensed:wght@700&display=swap">
<style>
  :root {
    --page-bg: #dfe4ea;
    --card-bg: #eef2f6;
    --navy: #1d3a74;
    --navy-light: #3f5f95;
    --stripe-blue: #3a8fd0;
    --stripe-green: #2e9a4c;
    --stripe-teal: #1f8a73;
    --stripe-gray: #8f93a3;
    --ink: #2f3337;
    --white: #ffffff;
    --icon-phone: #3d8d7a;
    --icon-mail: #34508a;
    --icon-web: #3f8a4a;
    --brand-dot: #7fa6c9;
  }
  * { margin: 0; padding: 0; box-sizing: border-box; }
  html, body { width: 1200px; height: 900px; overflow: hidden; }
  body { background: var(--page-bg); display: flex; align-items: center; justify-content: center; }
  .business-card {
    width: 1040px; height: 593px; display: block;
    box-shadow: 0 12px 30px rgba(20, 40, 80, 0.18);
  }
  .card-base { fill: var(--card-bg); }
  .header-band { fill: url(#bandShade); }
  .stripe-gray { fill: var(--stripe-gray); }
  .stripe-color { fill: url(#stripeShade); }
  .holder-name { font-family: "Roboto Condensed", "Roboto", sans-serif; font-weight: 700; font-size: 60px; fill: var(--white); letter-spacing: 1px; }
  .holder-role { font-family: "Roboto", sans-serif; font-weight: 500; font-size: 33px; fill: var(--white); }
  .role-rule { stroke: var(--white); stroke-width: 4; }
  .contact-text { font-family: "Roboto", sans-serif; font-weight: 500; font-size: 33px; fill: var(--ink); }
  .icon-phone { fill: var(--icon-phone); }
  .icon-mail { fill: var(--icon-mail); }
  .icon-web { fill: var(--icon-web); }
  .icon-glyph { fill: none; stroke: var(--white); stroke-width: 2.6; stroke-linecap: round; stroke-linejoin: round; }
  .strapline { font-family: "Roboto", sans-serif; font-weight: 500; font-size: 34px; fill: var(--ink); }
  .strap-rule { stroke: var(--ink); stroke-width: 2; }
  .brand-dot { fill: var(--brand-dot); }
  .brand-name { font-family: "Roboto", sans-serif; font-weight: 500; font-size: 42px; fill: var(--navy); letter-spacing: 1px; }
</style>
</head>
<body>
<svg class="business-card" viewBox="0 0 1383 788" xmlns="http://www.w3.org/2000/svg" aria-label="Lumivaleta business card for Moira Tess">
  <defs>
    <linearGradient id="bandShade" x1="0" y1="0" x2="1" y2="0">
      <stop offset="0" stop-color="var(--navy-light)"/>
      <stop offset="0.45" stop-color="var(--navy)"/>
      <stop offset="1" stop-color="var(--navy-light)"/>
    </linearGradient>
    <linearGradient id="stripeShade" x1="0" y1="0" x2="1" y2="0">
      <stop offset="0" stop-color="var(--stripe-blue)"/>
      <stop offset="0.3" stop-color="var(--stripe-green)"/>
      <stop offset="0.6" stop-color="var(--stripe-teal)"/>
      <stop offset="1" stop-color="var(--stripe-green)"/>
    </linearGradient>
  </defs>

  <rect class="card-base" width="1383" height="788"/>

  <!-- wave stripes -->
  <path class="stripe-color" d="M0 298 C180 330 380 352 560 348 C760 344 900 262 1060 222 C1200 190 1300 180 1383 176 L1383 200 C1300 204 1200 215 1080 245 C920 285 760 370 520 378 C340 384 160 355 0 330 Z"/>
  <path class="stripe-gray" d="M560 346 C760 340 900 258 1060 226 C1200 198 1300 196 1383 198 L1383 214 C1300 210 1200 216 1070 248 C910 290 760 352 560 352 Z"/>

  <!-- header band -->
  <path class="header-band" d="M0 0 H1383 V176 C1300 180 1200 190 1060 222 C900 262 760 344 560 348 C380 352 180 330 0 298 Z"/>

  <text class="holder-name" x="97" y="159">MOIRA TESS</text>
  <text class="holder-role" x="97" y="201">Energist</text>
  <line class="role-rule" x1="97" y1="223" x2="248" y2="223"/>

  <!-- contact rows -->
  <g class="contact-row">
    <rect class="icon-phone" x="97" y="462" width="44" height="44" rx="3"/>
    <path class="icon-glyph" d="M111 473 c-3 4 0 13 7 19 c6 5 12 6 14 3 l-4 -5 l-4 2 c-3 -2 -6 -5 -8 -9 l2 -4 z"/>
    <text class="contact-text" x="166" y="497">1-555-014-2786</text>
  </g>
  <g class="contact-row">
    <rect class="icon-mail" x="97" y="519" width="44" height="44" rx="3"/>
    <rect class="icon-glyph" x="107" y="531" width="24" height="18"/>
    <path class="icon-glyph" d="M107 531 l12 10 l12 -10"/>
    <text class="contact-text" x="166" y="554">mt@lumivaleta.example</text>
  </g>
  <g class="contact-row">
    <rect class="icon-web" x="97" y="576" width="44" height="44" rx="3"/>
    <circle class="icon-glyph" cx="119" cy="598" r="11"/>
    <path class="icon-glyph" d="M108 598 h22 M119 587 c-6 7 -6 15 0 22 M119 587 c6 7 6 15 0 22"/>
    <text class="contact-text" x="166" y="611">lumivaleta.example</text>
  </g>

  <!-- strapline -->
  <text class="strapline" x="97" y="714">Achieving Vibrational Equilibrium</text>
  <line class="strap-rule" x1="627" y1="714" x2="1383" y2="714"/>

  <!-- brand name -->
  <g class="brand-mark">
    <circle class="brand-dot" cx="942" cy="488" r="22"/>
    <text class="brand-name" x="980" y="503">LUMIVALETA</text>
  </g>
</svg>
</body>
</html>
```